New Business Card Design Project

We are looking for a talented individual to create a truly awesome/unique business card design for us. We are looking for a someone to design something that will really stand out from the crowd - we don't mind what ideas you come up with (ie embossed/flat/matte/shine etc etc) just wow us with your creativity.
Updates

Target Market(s)

Video Games Industry Professionals (all levels of seniority from QA Testers through to CEOs)

Contact Information for Business Card

Company logo (see upload)
Company name: Northbay Play Careers Ltd
Employee Name: Darren Elsby
Job title: CEO
Website: www.nbpc2go.example
Office +44 1632 960418
Mobile: +44 7700 900276
Email: darren@nbpc2go.example

Colors

Designer to choose colors to be used in the design.

Requirements
Must have
• The business card design MUST contain all the information listed in the BUSINESS CARD DETAILS box.
• You will see the colours that are relevant to us (ie company logo) in the uploaded imagery - however you do not have to use all these colours when designing the business card itself
• MUST BE DOUBLE SIDED

```html
<!DOCTYPE html>
<html lang="en">
<head>
<meta charset="utf-8">
<title>Northbay Play Careers – Business Card</title>
<link rel="stylesheet" href="https://fonts.googleapis.com/css2?family=Open+Sans:wght@400;600;700&display=swap">
<style>
  :root {
    --page-bg: #ededed;
    --card-dark: #2e2e30;
    --card-dark-deco: #3d3d40;
    --brand-orange: #f07d1a;
    --brand-navy: #1f2a6b;
    --paper-white: #ffffff;
    --title-grey: #8a8a8a;
    --text-light: #ffffff;
  }
  * { box-sizing: border-box; margin: 0; padding: 0; }
  html, body {
    width: 1200px; height: 1200px; overflow: hidden;
    background: var(--page-bg);
    font-family: "Open Sans", Arial, sans-serif;
  }
  .sheet {
    width: 1200px; height: 1200px;
    display: flex; flex-direction: column; align-items: center; justify-content: center;
    gap: 70px;
  }
  .card {
    position: relative;
    width: 880px; height: 500px;
    border-radius: 30px;
    overflow: hidden;
    background: var(--card-dark);
    box-shadow: 0 14px 30px rgba(0,0,0,0.22);
  }
  .card__decoration {
    position: absolute; inset: 0;
    background: radial-gradient(ellipse 46% 60% at 62% 40%, var(--card-dark-deco) 0%, rgba(61,61,64,0.5) 55%, rgba(46,46,48,0) 100%);
  }
  .brand {
    position: absolute;
    display: flex; align-items: center; gap: 18px;
    white-space: nowrap;
  }
  .brand__dot {
    flex: none;
    width: 58px; height: 58px; border-radius: 50%;
    background: var(--brand-navy);
    border: 3px solid var(--text-light);
  }
  .brand__name {
    font-weight: 700; color: var(--text-light);
    font-size: 40px; line-height: 1; letter-spacing: 0.5px;
  }
  .card--front .brand { left: 50%; top: 50%; transform: translate(-50%, -50%); }
  .card--back .brand { left: 50px; top: 225px; }
  .card--back .brand__name { font-size: 28px; }
  .card--back .brand__dot { width: 42px; height: 42px; }

  .card__panel { position: absolute; inset: 0; }
  .person {
    position: absolute; right: 40px; top: 44px; text-align: right; white-space: nowrap;
  }
  .person__name { color: var(--brand-orange); font-weight: 700; font-size: 38px; line-height: 1.1; }
  .person__title { color: var(--title-grey); font-weight: 400; font-size: 22px; margin-top: 2px; }

  .contact-list { position: absolute; right: 0; top: 190px; list-style: none; }
  .contact-item {
    height: 50px; margin-bottom: 10px;
    display: flex; align-items: center; justify-content: flex-end;
    gap: 12px; padding-right: 34px; white-space: nowrap;
    color: var(--text-light); font-size: 18px; font-weight: 400;
  }
  .contact-item svg { width: 20px; height: 20px; flex: none; }
</style>
</head>
<body>
<main class="sheet">

  <section class="card card--front" aria-label="Card front">
    <div class="card__decoration" role="img" aria-label="Faint large decorative mascot artwork in dark grey"></div>
    <div class="brand">
      <span class="brand__dot"></span>
      <span class="brand__name">Northbay Play Careers</span>
    </div>
  </section>

  <section class="card card--back" aria-label="Card back">
    <div class="card__decoration" role="img" aria-label="Faint large decorative mascot artwork in dark grey"></div>
    <svg class="card__panel" viewBox="0 0 880 500" width="880" height="500" aria-hidden="true">
      <polygon points="500,0 880,0 880,500 600,500" fill="var(--paper-white)"/>
      <polygon points="486,0 502,0 602,500 586,500" fill="var(--brand-orange)"/>
      <polygon points="538,190 880,190 880,240 548,240" fill="var(--brand-orange)"/>
      <polygon points="550,250 880,250 880,300 560,300" fill="var(--brand-orange)"/>
      <polygon points="562,310 880,310 880,360 572,360" fill="var(--brand-orange)"/>
      <polygon points="574,370 880,370 880,420 584,420" fill="var(--brand-orange)"/>
    </svg>

    <div class="brand">
      <span class="brand__dot"></span>
      <span class="brand__name">Northbay Play Careers</span>
    </div>

    <div class="person">
      <p class="person__name">Darren Elsby</p>
      <p class="person__title">CEO</p>
    </div>

    <ul class="contact-list">
      <li class="contact-item">+44 1632 960418
        <svg viewBox="0 0 24 24" aria-hidden="true"><path fill="#fff" d="M6.6 10.8a15 15 0 0 0 6.6 6.6l2.2-2.2c.3-.3.7-.4 1-.2 1.1.4 2.3.6 3.6.6.6 0 1 .4 1 1V20c0 .6-.4 1-1 1A17 17 0 0 1 3 4c0-.6.4-1 1-1h3.5c.6 0 1 .4 1 1 0 1.3.2 2.5.6 3.6.1.3 0 .7-.2 1z"/></svg>
      </li>
      <li class="contact-item">+44 7700 900276
        <svg viewBox="0 0 24 24" aria-hidden="true"><rect x="6" y="2" width="12" height="20" rx="2" fill="none" stroke="#fff" stroke-width="2"/><circle cx="12" cy="18" r="1.2" fill="#fff"/></svg>
      </li>
      <li class="contact-item">darren@nbpc2go.example
        <svg viewBox="0 0 24 24" aria-hidden="true"><rect x="2" y="5" width="20" height="14" rx="1" fill="#fff"/><path d="M2 6l10 7 10-7" fill="none" stroke="var(--brand-orange)" stroke-width="1.8"/></svg>
      </li>
      <li class="contact-item">www.nbpc2go.example</li>
    </ul>
  </section>

</main>
</body>
</html>
```